Office brochure for chronic pain doctor

I need an brochure for my office, and since I want to be able to mail the brochure, I think trifold would be the best size. I treat patients with chronic head and neck pain, as well as sleep apnea. I treat all of the following:

1. headaches
2. myofascial pain, which is a fancy way of saying muscle pain
3. neuropathic pain, which is a fancy way of saying nerve pain
4. TMJ, which stands for the temporomandibular joint (jaw joint)
5. obstructive sleep apnea

The colors will be based on my logo on my website, which you can see at www.BrightJPR.net, and you can learn more about what I do at my website. JPR stands for orofacial pain, which is a speciality training within the field of dentistry but I do not treat teeth. I have high resolution graphics for the brochure so I need someone with an artistic eye to design and lay out the brochure.

The logo colors are:
Purple 9e80bb
Pink f6b1d0
Blue 0f4b8f
Updates

I had a request for the logo in a .ai or .pdf format, which I have just uploaded. Please let me know if you have any other requests. Thank you, Dale

Target Market(s)

80% female, 20% male. I am in an upscale area of Los Angeles called Beverly Hills but I will see a patient from any area around Los Angeles or from any area in the world.

Industry/Entity Type

Training

Colors
6b449b
e567a6
0355a3

Requirements
Must have
• I want a small section of the brochure to feature each of the five areas I treat, and I have included an image to place in each of the five sections. A small section should include a short bio of me, which you can condense from www.brightjpr.net/dale. The brochure must appeal to women since 80% of my patients are female but I don't want to completely ignore men. Most of the pain patients are female, and most of the sleep apnea patients are male.

Here are the colors in my logo
Purple 9e80bb
Pink f6b1d0
Blue 0f4b8f
Should not have
• Anything related to teeth or dentistry.
No decorative or script fonts.

```html
<!DOCTYPE html>
<html lang="en">
<head>
<meta charset="utf-8">
<title>Caring for Head Pain and Sleep Apnea – Trifold Brochure</title>
<link href="https://fonts.googleapis.com/css2?family=Arimo:wght@400;700&display=swap" rel="stylesheet">
<style>
  :root{
    --bg:#eeeeee;
    --paper:#f4f4f5;
    --paper-shade:#e4e4e6;
    --purple:#9e80bb;
    --pink:#f1a8cb;
    --blue:#0f4b8f;
    --ink-blue:#1f3f8a;
    --navy-top:#8a8b98;
    --navy:#1d1e42;
    --navy-deep:#16163a;
    --quote:#b3a3d6;
    --quote-pink:#f3b3d1;
    --white:#ffffff;
    --art-light:#e6dcd8;
    --art-mid:#cdb8b0;
    --art-deep:#b39a90;
  }
  *{box-sizing:border-box;margin:0;padding:0}
  html,body{width:1200px;height:1000px;overflow:hidden}
  body{background:var(--bg);font-family:"Arimo",Arial,sans-serif;position:relative}

  .inside-spread{
    position:absolute;left:40px;top:190px;width:800px;height:620px;
    display:grid;grid-template-columns:repeat(3,1fr);
    background:var(--paper);
    box-shadow:0 10px 30px rgba(0,0,0,.18);
  }
  .panel{position:relative;padding:22px 18px 0;border-right:1px solid var(--paper-shade);overflow:hidden}
  .panel:last-child{border-right:none}

  .section-header{
    display:block;width:120px;color:var(--white);font-weight:700;font-size:13px;line-height:1;
    padding:6px 12px;margin-bottom:8px;
  }
  .section-header--purple{background:var(--purple)}
  .section-header--pink{background:var(--pink)}
  .section-header--blue{background:var(--blue)}

  .body-copy{color:var(--ink-blue);font-size:10.5px;line-height:1.3;text-align:justify;margin-bottom:12px}

  .art{display:block;background:linear-gradient(160deg,var(--art-light),var(--art-mid) 60%,var(--art-deep))}
  .art--muscle-head{position:absolute;left:18px;bottom:0;width:212px;height:260px}
  .art--headache{width:130px;height:115px;margin:6px auto 18px}
  .art--nerve-map{width:130px;height:120px;margin:6px auto 0}
  .art--jaw-joint{width:120px;height:105px;margin:4px 0 18px auto}
  .art--airway{position:absolute;right:0;bottom:0;width:220px;height:145px}

  .cover{
    position:absolute;left:880px;top:190px;width:270px;height:620px;
    background:linear-gradient(180deg,var(--navy-top) 0%,var(--navy) 28%,var(--navy-deep) 100%);
    box-shadow:0 10px 30px rgba(0,0,0,.25);
    padding:110px 22px 0;color:var(--white);
  }
  .brand{display:flex;align-items:center;justify-content:center;gap:10px;margin-bottom:26px}
  .brand-mark{width:26px;height:26px;background:var(--pink)}
  .brand-name{font-weight:700;font-size:30px;color:var(--white);letter-spacing:2px}
  .cover-title{font-weight:700;font-size:24px;line-height:1.15;text-align:center;letter-spacing:1.5px}
  .testimonial{position:absolute;left:22px;right:22px;top:410px}
  .testimonial-quote{color:var(--quote);font-size:13px;line-height:1.3;text-align:justify}
  .testimonial-author{color:var(--quote-pink);font-size:12px;text-align:right;margin-top:10px}
</style>
</head>
<body>
  <section class="inside-spread">
    <article class="panel panel--intro">
      <h2 class="section-header section-header--purple">Header</h2>
      <p class="body-copy">Lorem ipsum dolor sit amet, consectetur adipisicing elit, sed do eiusmod tempor incididunt ut labore et dolore magna aliqua. Ut enim ad minim veniam, quis nostrud exercitation ullamco laboris nisi ut aliquip ex ea commodo consequat. Duis aute irure dolor in reprehenderit in voluptate velit esse cillum dolore eu fugiat nulla pariatur. Excepteur sint occaecat cupidatat non proident, sunt in culpa qui officia deserunt mollit anim id est.</p>
      <p class="body-copy">Lorem ipsum dolor sit amet, consectetur adipisicing elit, sed do eiusmod tempor incididunt ut labore et dolore magna aliqua. Ut enim ad minim veniam, quis nostrud exercitation ullamco laboris nisi ut aliquip ex ea commodo consequat. Duis aute irure dolor in reprehenderit in voluptate velit esse cillum dolore eu fugiat nulla pariatur. Excepteur sint occaecat cupidatat non proident, sunt in culpa qui officia deserunt mollit anim id est.</p>
      <div class="art art--muscle-head" role="img" aria-label="Anatomical illustration of head and neck muscles in profile"></div>
    </article>

    <article class="panel panel--pain">
      <h2 class="section-header section-header--pink">Header</h2>
      <p class="body-copy">Lorem ipsum dolor sit amet, consectetur adipisicing elit, sed do eiusmod tempor incididunt ut labore et dolore magna aliqua. Ut enim ad minim veniam, quis nostrud exercitation ullamco laboris nisi ut aliquip ex ea commodo consequat. Duis aute irure dolor in reprehenderit in voluptate velit.</p>
      <div class="art art--headache" role="img" aria-label="Illustration showing where headache pain is felt"></div>
      <h2 class="section-header section-header--pink">Header</h2>
      <p class="body-copy">Lorem ipsum dolor sit amet, consectetur adipisicing elit, sed do eiusmod tempor incididunt ut labore et dolore magna aliqua. Ut enim ad minim veniam, quis nostrud exercitation ullamco laboris nisi ut aliquip ex ea commodo consequat. Duis aute irure dolor in reprehenderit in voluptate velit.</p>
      <div class="art art--nerve-map" role="img" aria-label="Illustration of facial nerve pain zones"></div>
    </article>

    <article class="panel panel--jaw-sleep">
      <h2 class="section-header section-header--blue">Header</h2>
      <p class="body-copy">Lorem ipsum dolor sit amet, consectetur adipisicing elit, sed do eiusmod tempor incididunt ut labore et dolore magna aliqua. Ut enim ad minim veniam, quis nostrud exercitation ullamco laboris nisi ut aliquip ex ea commodo consequat. Duis aute irure dolor in reprehenderit in voluptate velit.</p>
      <div class="art art--jaw-joint" role="img" aria-label="Anatomical illustration of the jaw joint"></div>
      <h2 class="section-header section-header--blue">Header</h2>
      <p class="body-copy">Lorem ipsum dolor sit amet, consectetur adipisicing elit, sed do eiusmod tempor incididunt ut labore et dolore magna aliqua. Ut enim ad minim veniam, quis nostrud exercitation ullamco laboris nisi ut aliquip ex ea commodo consequat. Duis aute irure dolor in reprehenderit in voluptate velit esse cillum dolore eu fugiat nulla pariatur. Excepteur sint occaecat cupidatat non proident, sunt in culpa qui officia deserunt mollit anim id est.</p>
      <div class="art art--airway" role="img" aria-label="Illustration of a sleeping patient showing the blocked airway"></div>
    </article>
  </section>

  <section class="cover">
    <div class="brand">
      <span class="brand-mark"></span>
      <span class="brand-name">JPR</span>
    </div>
    <h1 class="cover-title">Caring for<br>Head Pain and<br>Sleep Apnea</h1>
    <blockquote class="testimonial">
      <p class="testimonial-quote">"I had TMJ pain for 15 years and spent a lot of time and money being treated for "TMJ" until Dr. Marlowe correctly diagnosed that my pain was not from my joint, it was caused by muscles. I wish all doctors did as through an exam as Dr. Marlowe."</p>
      <p class="testimonial-author">Noreen, K. Los Angeles, California</p>
    </blockquote>
  </section>
</body>
</html>
```